Business Card Design Project - bel soravin group

dear Sirs

we need business card design for our group ( BEL Soravin Group ) , i have got the Logo design of our group from pixel harbor in previous , so all need details relating to our group i think available with you, as well as the the chosen logo design

we hope to provide us with business card logo that to be appropaite and satisfactory to us .

thanks

note : logo design of our group is attached .
Updates

Reason: please extend the deadline of my project for additional 15 days because i didn't received appropriate design for our gruop yet . kindly beaware that i have received 77 design till now , supossed to send me 200-250 design at least . thanks

Target Market(s)

contents
-

name : Korvan EL Mistrani

position : Operation Manager

Industry/Entity Type

Business

Requirements
Must have

• person name

group logo
Nice to have
• logo color matching with back background

```html
<!DOCTYPE html>
<html lang="en">
<head>
<meta charset="utf-8">
<title>BEL Soravin Group – Business Card</title>
<link href="https://fonts.googleapis.com/css2?family=Source+Sans+3:wght@400;600;700&display=swap" rel="stylesheet">
<style>
  :root {
    --page: #ffffff;
    --card-white: #ffffff;
    --card-black: #0b0b0b;
    --brand-blue: #134a8a;
    --brand-gold: #c2962f;
    --text-dark: #3a3a3a;
    --text-light: #ffffff;
    --shadow: rgba(0, 0, 0, 0.45);
  }
  * { margin: 0; padding: 0; box-sizing: border-box; }
  html, body {
    width: 1200px; height: 900px; overflow: hidden;
    background: var(--page);
    font-family: "Source Sans 3", sans-serif;
  }
  .sheet { position: relative; width: 1200px; height: 900px; }
  .card {
    position: absolute; left: 304px; width: 629px; height: 360px;
    box-shadow: 4px 5px 8px var(--shadow);
    overflow: hidden;
  }
  .card--front { top: 57px; background: var(--card-white); }
  .card--back { top: 470px; background: var(--card-black); }

  .brand {
    position: absolute; display: flex; align-items: center; gap: 12px;
    color: var(--brand-blue); font-weight: 600; font-size: 32px;
    letter-spacing: 0.5px; white-space: nowrap;
  }
  .brand__mark { width: 18px; height: 18px; background: var(--brand-gold); }
  .card--front .brand { right: 50px; top: 68px; }
  .card--back .brand { left: 50%; top: 140px; transform: translateX(-50%); font-size: 40px; }
  .card--back .brand__mark { width: 22px; height: 22px; }

  .person { position: absolute; left: 39px; top: 146px; }
  .person__name { font-size: 22px; font-weight: 700; color: var(--brand-blue); line-height: 1.1; }
  .person__role { font-size: 15px; color: var(--text-dark); margin-top: 3px; }

  .contact { position: absolute; left: 39px; top: 232px; list-style: none; }
  .contact__item {
    display: flex; align-items: center; gap: 7px;
    font-size: 15px; color: var(--text-dark); height: 21px;
  }
  .contact__icon { width: 13px; height: 13px; flex: none; }

  .band { position: absolute; left: 0; bottom: 0; width: 629px; height: 30px; }
  .band svg { position: absolute; inset: 0; }
  .band__address, .band__web {
    position: absolute; top: 0; line-height: 30px; font-size: 15px; color: var(--text-light);
  }
  .band__address { left: 39px; }
  .band__web { right: 58px; }

  .back__web {
    position: absolute; left: 0; right: 0; top: 296px; text-align: center;
    font-size: 20px; color: var(--text-light);
  }
</style>
</head>
<body>
<main class="sheet">
  <section class="card card--front">
    <div class="brand"><span class="brand__mark"></span>BEL Soravin Group</div>

    <div class="person">
      <div class="person__name">Korvan EL Mistrani</div>
      <div class="person__role">Operation Manager</div>
    </div>

    <ul class="contact">
      <li class="contact__item">
        <svg class="contact__icon" viewBox="0 0 12 12"><circle cx="6" cy="6" r="6" fill="var(--brand-blue)"/><path d="M3.6 3.2l1.3-.4.7 1.5-.8.6c.4.9 1 1.5 1.9 1.9l.6-.8 1.5.7-.4 1.3c-2.7-.2-4.6-2.1-4.8-4.8z" fill="#fff"/></svg>
        02 5550 1842
      </li>
      <li class="contact__item">
        <svg class="contact__icon" viewBox="0 0 12 12"><circle cx="6" cy="6" r="6" fill="var(--brand-blue)"/><rect x="3" y="5" width="6" height="3.2" fill="#fff"/><rect x="4" y="3" width="4" height="2" fill="#fff"/></svg>
        02 5550 1843
      </li>
      <li class="contact__item">
        <svg class="contact__icon" viewBox="0 0 12 12"><circle cx="6" cy="6" r="6" fill="var(--brand-blue)"/><rect x="3.8" y="2.6" width="4.4" height="6.8" rx="0.8" fill="#fff"/><rect x="4.6" y="3.6" width="2.8" height="3.8" fill="var(--brand-blue)"/></svg>
        02 5550 1844
      </li>
      <li class="contact__item">
        <svg class="contact__icon" viewBox="0 0 12 12"><circle cx="6" cy="6" r="6" fill="var(--brand-blue)"/><rect x="2.8" y="3.8" width="6.4" height="4.4" fill="#fff"/><path d="M2.8 3.8L6 6.4l3.2-2.6" fill="none" stroke="var(--brand-blue)" stroke-width="0.8"/></svg>
        korvan@belsoravin.com
      </li>
    </ul>

    <div class="band">
      <svg viewBox="0 0 629 30" width="629" height="30">
        <polygon points="0,0 392,0 380,30 0,30" fill="var(--brand-blue)"/>
        <polygon points="397,0 629,0 629,30 385,30" fill="var(--brand-gold)"/>
      </svg>
      <span class="band__address">P.O. Box 418, Elmsworth, Vic, 3190</span>
      <span class="band__web">www.belsoravin.com</span>
    </div>
  </section>

  <section class="card card--back">
    <div class="brand"><span class="brand__mark"></span>BEL Soravin Group</div>
    <div class="back__web">www.belsoravin.com</div>
  </section>
</main>
</body>
</html>
```